hair salon logo and Business Card Design

this logo needs to reflect a vibrant, trendy and fun business, targeting 20 to 50 year old ladies in a nice sunny part of Australia.Our aim is to make everyone feel in a fantastic mood when they walk out of the salon,and look equally glamorous.
I would like the logo to be simple yet using bold colors and font.
ideally the name mirra would be lowercase with a nice rounded shape and hair+beauty, with upper case and the letter i in an inverted position.

Industry/Entity Type

Hair

Contact Information for Business Card

mirra
hair | beauty.

Lia Forsett
stylist/owner
0419376052
58 Wexcombe St. Bayvale QLD. 4032

Requirements
Must have
• front all the business details
back lined for writing notes.
Nice to have
• use of bold stand out colors, simple shapes sense of movement, not stillness, modern, professional.

```html
<!DOCTYPE html>
<html lang="en">
<head>
<meta charset="utf-8">
<title>mirra hair | beauty — Business Card</title>
<link rel="stylesheet" href="https://fonts.googleapis.com/css2?family=Questrial&family=Roboto:wght@400;700&display=swap">
<style>
  :root {
    --cream: #fbf6ef;
    --teal: #00a0b0;
    --peach: #ffc48c;
    --brown: #5a2a0a;
    --grey: #9a9ca0;
  }
  html, body {
    margin: 0;
    padding: 0;
    overflow: hidden;
    background: var(--cream);
  }
  .card {
    position: relative;
    width: 1200px;
    height: 740px;
    background: var(--cream);
    overflow: hidden;
    font-family: "Roboto", Arial, sans-serif;
  }
  .card p { margin: 0; line-height: 1; white-space: nowrap; }
  .sunburst {
    position: absolute;
    left: 708px;
    top: 0;
    width: 492px;
    height: 492px;
  }
  .brand-name {
    position: absolute;
    left: 92px;
    top: 102px;
    margin: 0;
    font-family: "Questrial", Arial, sans-serif;
    font-weight: 400;
    font-size: 190px;
    line-height: 1;
    letter-spacing: -2px;
    color: var(--teal);
  }
  .brand-line {
    position: absolute;
    left: 94px;
    top: 278px;
    font-family: "Questrial", Arial, sans-serif;
    font-size: 44px;
    color: var(--brown);
  }
  .person-name {
    position: absolute;
    left: 96px;
    top: 359px;
    font-size: 56px;
    font-weight: 700;
    letter-spacing: -1px;
    color: var(--brown);
  }
  .person-role {
    position: absolute;
    left: 97px;
    top: 411px;
    font-size: 46px;
    font-weight: 400;
    color: var(--grey);
  }
  .role-dot {
    display: inline-block;
    width: 11px;
    height: 11px;
    margin: 0 10px 6px;
    background: var(--teal);
    vertical-align: middle;
  }
  .phone {
    position: absolute;
    left: 96px;
    top: 486px;
    font-size: 50px;
    font-weight: 700;
    color: var(--grey);
  }
  .address {
    position: absolute;
    left: 94px;
    top: 578px;
    font-family: "Questrial", Arial, sans-serif;
    font-size: 44px;
    color: var(--grey);
  }
  .footer-band {
    position: absolute;
    left: 0;
    top: 649px;
    width: 1200px;
    height: 91px;
    background: var(--teal);
  }
</style>
</head>
<body>
  <div class="card">
    <svg class="sunburst" viewBox="0 0 492 492" role="img" aria-label="Decorative peach sunburst of dots radiating from the centre">
      <defs>
        <radialGradient id="sunGlow" cx="50%" cy="50%" r="50%">
          <stop offset="0%" stop-color="#ffc48c" stop-opacity="0.95"/>
          <stop offset="60%" stop-color="#ffc48c" stop-opacity="0.6"/>
          <stop offset="100%" stop-color="#ffc48c" stop-opacity="0"/>
        </radialGradient>
      </defs>
      <circle cx="271" cy="223" r="250" fill="url(#sunGlow)"/>
    </svg>

    <h1 class="brand-name">mirra</h1>
    <p class="brand-line">mirra hair | beauty</p>

    <p class="person-name">Lia Forsett</p>
    <p class="person-role">stylist<span class="role-dot"></span>owner</p>

    <p class="phone">0419 376 052</p>
    <p class="address">58 Wexcombe Street, Bayvale, QLD 4032</p>

    <div class="footer-band"></div>
  </div>
</body>
</html>
```